Heronby Mortgage Capital Business Card

We need a business card design for our mortgage servicing company. In addition to servicing the loans of homeowners, we help homeowners with purchasing their homes and any mortgage refinancing. We would like to see designs that use the colors in the logo attached below (gold-ish yellow and navy blue), and any other design you deem fit! The design should communicate a simpler life with smart mortgages provided by Heronby.

```html
<!DOCTYPE html>
<html lang="en">
<head>
<meta charset="utf-8">
<title>Heronby Mortgage Capital – Business Card</title>
<link rel="stylesheet" href="https://fonts.googleapis.com/css2?family=Montserrat:wght@400;500;700;800&family=Source+Sans+3:wght@400&display=swap">
<style>
  :root {
    --backdrop: #d1cfbd;
    --navy: #332c55;
    --gold: #d6a93a;
    --paper: #ffffff;
    --ink: #2a2547;
  }
  * { box-sizing: border-box; margin: 0; padding: 0; }
  html, body { width: 1200px; height: 801px; overflow: hidden; }
  body {
    position: relative;
    background: var(--backdrop);
    font-family: "Montserrat", sans-serif;
    color: var(--ink);
  }

  .card { position: absolute; overflow: hidden; box-shadow: 2px 3px 6px rgba(0,0,0,.12); }

  /* Front */
  .card--front { left: 357px; top: 90px; width: 485px; height: 299px; background: var(--navy); }
  .front-brand {
    position: absolute; left: 0; right: 0; top: 118px;
    text-align: center;
    font-weight: 700; font-size: 36px; letter-spacing: .5px;
    color: var(--gold);
  }
  .front-band { position: absolute; left: 0; top: 0; width: 485px; height: 299px; }
  .front-url {
    position: absolute; left: 132px; width: 220px; top: 245px;
    text-align: center; font-size: 13px; font-weight: 500; color: var(--navy);
  }

  /* Back */
  .card--back { left: 356px; top: 428px; width: 488px; height: 301px; background: var(--paper); }
  .back-strip { position: absolute; left: 0; top: 0; width: 140px; height: 100%; background: var(--navy); }
  .back-info { position: absolute; left: 169px; top: 22px; }
  .holder-name { font-weight: 800; font-size: 27px; letter-spacing: .6px; color: var(--ink); line-height: 1.1; }
  .holder-role { font-family: "Source Sans 3", sans-serif; font-size: 19px; color: var(--ink); margin-top: 2px; }
  .contact-group { margin-top: 20px; font-size: 13px; line-height: 21px; color: #1d1a30; }
  .contact-group--web { margin-top: 24px; line-height: 16px; }
  .contact-group--address { margin-top: 26px; line-height: 20px; }
  .back-brand {
    position: absolute; right: 16px; bottom: 18px;
    font-weight: 700; font-size: 15px; color: var(--navy);
  }
</style>
</head>
<body>

  <section class="card card--front" aria-label="Card front">
    <svg class="front-band" viewBox="0 0 485 299" aria-hidden="true">
      <rect x="0" y="249" width="485" height="11" fill="var(--gold)"/>
      <polygon points="137,240 353,240 347,270 132,273" fill="var(--gold)"/>
    </svg>
    <div class="front-brand">Heronby Mortgage</div>
    <div class="front-url">www.yoursite.com</div>
  </section>

  <section class="card card--back" aria-label="Card back">
    <div class="back-strip"></div>
    <div class="back-info">
      <h1 class="holder-name">JOHHNY DOE</h1>
      <p class="holder-role">Graphic designer</p>
      <div class="contact-group contact-group--phone">
        <p>+00 1234 4567</p>
        <p>+00 1234 4567</p>
      </div>
      <div class="contact-group contact-group--web">
        <p>www.yoursite.com</p>
        <p>your@email.com</p>
      </div>
      <div class="contact-group contact-group--address">
        <p>you ciry address street</p>
        <p>location, Canada city, uk</p>
      </div>
    </div>
    <div class="back-brand">Heronby Mortgage</div>
  </section>

</body>
</html>
```